data and media shredding company needs a flyer design

We need a flyer design for a startup company based on Long Island, NY. We shred all types of storage devices at the customers location. We want to emphasize on the dangers of identity theft and confidential information. With some focus on e-waste recycling. We want to coordinate the flyer with our website design.
www.vaultmincerservices.example

Target Market(s)

business owners that have personal information that needs to be destroyed

Font styles to use
Sans Serif

Colors

Designer to choose colors to be used in the design.

Requirements
Must have
• must have company name and logo, must have web address, must have phone number 855-310-4968, must have briefing of what we do, must be set for a trifold flyer

```html
<!DOCTYPE html>
<html lang="en">
<head>
<meta charset="utf-8">
<title>Vault Mincer Services – Trifold Cover</title>
<link rel="stylesheet" href="https://fonts.googleapis.com/css2?family=Jost:wght@400;500;700&display=swap">
<style>
  :root {
    --backdrop: #b3b3b3;
    --navy: #232a3f;
    --navy-deep: #1f2538;
    --green: #7cc242;
    --green-dark: #4f9a2c;
    --photo-light: #d9dcd8;
    --photo-mid: #9aa39a;
    --white: #ffffff;
    --ink: #2b2f3a;
    --muted: #c8ccd6;
  }
  * { margin: 0; padding: 0; box-sizing: border-box; }
  html, body { width: 1200px; height: 930px; overflow: hidden; }
  body { background: var(--backdrop); font-family: "Jost", Arial, sans-serif; }

  .brochure {
    position: absolute; left: 60px; top: 70px;
    width: 1080px; height: 790px;
    display: flex;
  }
  .panel-flap { width: 340px; height: 100%; background: var(--navy-deep); }
  .panel-spread { position: relative; width: 740px; height: 100%; }
  .spread-art { position: absolute; inset: 0; }

  .brand { display: flex; align-items: center; gap: 8px; }
  .brand-dot {
    width: 26px; height: 26px; border-radius: 50%;
    border: 2px solid var(--green);
  }
  .brand-name { font-weight: 500; font-size: 15px; color: var(--green); white-space: nowrap; }

  .back-contact { position: absolute; left: 100px; top: 410px; width: 186px; }
  .back-contact .brand { padding-bottom: 12px; border-bottom: 2px solid var(--green); }

  .contact-list { list-style: none; font-size: 10.5px; line-height: 1.25; margin-top: 12px; }
  .contact-list li { display: flex; gap: 10px; }
  .contact-list .label { font-weight: 700; width: 32px; }
  .back-contact .contact-list { color: var(--muted); }

  .headline {
    position: absolute; left: 403px; top: 335px;
    color: var(--white); font-weight: 700; font-size: 56px; line-height: 62px;
    letter-spacing: -0.5px;
  }

  .front-footer {
    position: absolute; left: 400px; top: 705px; width: 330px;
    display: flex; align-items: center; gap: 14px;
  }
  .front-footer .brand-name { font-size: 13px; color: var(--green-dark); }
  .front-footer .brand-dot { width: 24px; height: 24px; border-color: var(--green-dark); }
  .footer-divider { width: 2px; height: 40px; background: var(--green-dark); }
  .front-footer .contact-list { margin-top: 0; color: var(--ink); font-size: 9.5px; }
  .front-footer .contact-list .label { width: 30px; }
</style>
</head>
<body>
  <main class="brochure">
    <section class="panel-flap" aria-label="Inner flap"></section>

    <section class="panel-spread">
      <svg class="spread-art" width="740" height="790" viewBox="0 0 740 790">
        <defs>
          <linearGradient id="photoTone" x1="0" y1="0" x2="1" y2="1">
            <stop offset="0" stop-color="#eef0ee"/>
            <stop offset="0.5" stop-color="var(--photo-mid)"/>
            <stop offset="1" stop-color="#5e665e"/>
          </linearGradient>
          <linearGradient id="backShade" x1="0" y1="0" x2="1" y2="0">
            <stop offset="0" stop-color="#262d44"/>
            <stop offset="1" stop-color="#1f2538"/>
          </linearGradient>
        </defs>
        <!-- back panel -->
        <rect class="back-panel" x="0" y="0" width="378" height="790" fill="url(#backShade)"/>
        <!-- front panel -->
        <rect class="front-panel" x="378" y="0" width="362" height="790" fill="var(--white)"/>
        <!-- photo area across the fold -->
        <polygon role="img" aria-label="Photo of two colleagues talking at a meeting table"
          points="140,0 633,0 741,196 741,670 455,670 378,525 378,455" fill="url(#photoTone)"/>
        <!-- thin light edge along diagonal -->
        <polygon points="116,0 140,0 378,455 378,498" fill="#c9ccd1" opacity="0.8"/>
        <!-- green diagonal bands -->
        <polygon points="168,0 378,0 378,400" fill="var(--green)" opacity="0.72"/>
        <polygon points="378,0 480,0 700,530 560,530 378,160" fill="var(--green)" opacity="0.75"/>
        <!-- back dark wedge over photo -->
        <polygon points="0,0 116,0 378,498 378,790 0,790" fill="url(#backShade)"/>
        <!-- white corner top right -->
        <polygon points="633,0 741,0 741,196" fill="var(--white)"/>
      </svg>

      <div class="back-contact">
        <div class="brand"><span class="brand-dot"></span><span class="brand-name">Vault Mincer Services</span></div>
        <ul class="contact-list">
          <li><span class="label">Tel.</span><span>855-310-4968</span></li>
          <li><span class="label">Email.</span><span>info@vaultmincerservices.example</span></li>
          <li><span class="label">Web.</span><span>vaultmincerservices.example</span></li>
        </ul>
      </div>

      <h1 class="headline">Keep Your<br>Information<br>Safe</h1>

      <div class="front-footer">
        <div class="brand"><span class="brand-dot"></span><span class="brand-name">Vault Mincer Services</span></div>
        <span class="footer-divider"></span>
        <ul class="contact-list">
          <li><span class="label">Tel.</span><span>855-310-4968</span></li>
          <li><span class="label">Email.</span><span>info@vaultmincerservices.example</span></li>
          <li><span class="label">Web.</span><span>vaultmincerservices.example</span></li>
        </ul>
      </div>
    </section>
  </main>
</body>
</html>
```